Flyer-Design für ein Montessori Familienzentrum
Super Zusammenarbeit :) Meine Wünsche und Ideen wurden sehr passend und schnell umgesetzt und miteinbezogen in das Design.
Zielgruppe
Wir sind ein Montessori Familienzentrum mit folgendem Angebot:
- Montessori Eltern-Kind-Gruppen für Babys ab 8 Wochen - 4 Jahren
- Montessori Coaching
- Stoffwindel- und Windelfrei Beratung
- Beratung zur Babygeleiteten Beikost
- Workshops für Eltern
Aufgabenstellung
Schlicht, Informativ, Überblick über die Angebote

```html
<!DOCTYPE html>
<html lang="de">
<head>
<meta charset="utf-8">
<title>Waldknirps – Montessori Eltern-Kind-Kurse Flyer</title>
<link rel="stylesheet" href="https://fonts.googleapis.com/css2?family=Jost:ital,wght@0,300;0,400;1,300;1,400&family=Nunito:ital,wght@1,800&family=Playfair+Display:wght@400;700&family=Great+Vibes&display=swap">
<style>
  :root{
    --stage:#9d9d9d;
    --paper:#ffffff;
    --shade:#f1f1f1;
    --ink:#555555;
    --ink-soft:#6a6a6a;
    --green:#4b7a34;
    --orange:#e87a3c;
  }
  *{margin:0;padding:0;box-sizing:border-box}
  html,body{width:1173px;height:1200px;overflow:hidden;background:var(--stage)}
  body{font-family:'Jost',sans-serif;color:var(--ink);font-weight:300}
  .canvas{position:relative;width:1173px;height:1200px;background:var(--stage);overflow:hidden}
  .panel{position:absolute;left:17px;width:1139px;background:var(--paper);overflow:hidden}
  .panel--outside{top:18px;height:569px}
  .panel--inside{top:610px;height:570px}
  .panel > *{position:absolute}
  .backdrop{left:0;top:0}

  .letter{left:24px;top:14px;width:282px;font-size:9.4px;line-height:12.9px;text-align:justify;hyphens:auto}
  .signature{left:186px;top:214px;font-family:'Great Vibes',cursive;font-size:23px;color:var(--ink)}
  .founder-name{left:75px;top:257px;font-size:21px;font-weight:300;letter-spacing:.5px;color:var(--ink)}
  .founder-titles{left:127px;top:289px;width:200px;font-size:10px;line-height:14.6px;font-style:italic}

  .brand{left:605px;top:80px;display:flex;align-items:center;gap:6px;font-size:13px;font-weight:400;color:var(--green);letter-spacing:1px}
  .brand-dot{width:12px;height:12px;border-radius:50%;background:var(--green)}

  .hero-photo{left:704px;top:25px;width:345px;height:382px;border-radius:50%;
    background:radial-gradient(ellipse at 55% 50%, #d9a98f 0%, #e8c4b4 30%, #f1dcd2 55%, rgba(255,255,255,0) 75%)}

  .title-main{left:645px;top:397px;font-family:'Playfair Display',serif;font-weight:700;font-size:37px;line-height:40px;color:var(--green)}
  .title-sub{left:645px;top:436px;font-family:'Playfair Display',serif;font-weight:400;font-size:30px;line-height:32px;color:var(--green)}
  .tagline{left:648px;top:477px;font-size:10px;letter-spacing:2px;font-weight:400;color:var(--ink)}
  .age-range{left:853px;top:500px;font-size:10px;letter-spacing:2px;font-weight:400;color:var(--orange)}
  .contact{top:546px;font-size:7.6px;letter-spacing:1.1px;font-weight:400;color:var(--ink);white-space:nowrap}

  .section-title{font-family:'Nunito',sans-serif;font-style:italic;font-weight:800;color:var(--orange);white-space:nowrap}
  .advice-title{left:14px;top:375px;font-size:24px}
  .offer{font-size:9.2px;line-height:12.6px}
  .offer h3{font-size:15px;line-height:19px;font-weight:300;font-style:italic;color:var(--ink);margin-bottom:4px}
  .offer p{margin-bottom:8px}
  .offer ul{list-style:none;margin-left:23px;font-size:9.6px;line-height:13px}
  .offer li::before{content:"• ";font-size:7px;vertical-align:1px}
  .offer--diapers{left:18px;top:426px;width:250px}
  .offer--food{left:294px;top:424px;width:255px}

  .kicker{font-style:italic;font-size:14px;line-height:18px;font-weight:300;text-align:right}
  .topic h3{font-size:17px;line-height:20px;font-weight:400;color:var(--green);letter-spacing:.4px}
  .topic .topic-sub{font-size:12px;line-height:14px;font-style:italic;color:var(--orange);text-align:right;margin-bottom:5px}
  .topic p{font-size:9.4px;line-height:12.7px;text-align:justify}

  .course h3{font-size:17px;line-height:20px;font-weight:400;color:var(--green);letter-spacing:.4px}
  .course .course-sub{font-size:12px;line-height:14px;font-style:italic;color:var(--orange);margin-bottom:5px}
  .course p{font-size:9.2px;line-height:12.7px;text-align:justify}

  .coaching-title{left:198px;top:392px;font-size:22px;line-height:28px}
  .coaching-kicker{left:262px;top:421px;width:300px}
  .coaching p{font-size:9.4px;line-height:13px;margin-bottom:7px}
  .footer-line{left:593px;top:550px;font-size:10.5px;letter-spacing:1.5px;font-weight:400;color:#333}
</style>
</head>
<body>
<div class="canvas">

  <!-- Outer side: founder, advice, cover -->
  <section class="panel panel--outside">
    <svg class="backdrop" width="1139" height="569" viewBox="0 0 1139 569" aria-hidden="true">
      <polygon points="0,285 570,470 570,569 0,569" fill="var(--shade)"/>
      <polygon points="570,505 1139,230 1139,569 570,569" fill="var(--shade)" opacity=".7"/>
      <polygon points="600,0 760,0 600,110" fill="var(--shade)"/>
    </svg>

    <p class="letter">Hallo,<br>mein Name ist Carolina, ich bin Jahrgang 1994, verheiratet und wohne mit meiner Familie in Lindenau. Ich bin staatlich anerkannte Erzieherin und habe nach meiner Ausbildungszeit zunächst ein Jahr in Amerika gelebt und gearbeitet und danach in einer normalen und einer integrativen Kinderkrippe. Die Waldknirps habe ich im September 2020 gegründet und seit September 2021 hat das Kurskonzept einen Montessori Schwerpunkt.<br>Neben meiner Fortbildung zur Montessori Spielgruppenleiterin bei Helena Marks und zahlreichen Fortbildungen zum Montessori Kinderhaus Material, mache ich derzeit noch zusätzlich mein Montessori Diplom für Kleinkinder an der Montessori Akademie in Graz. Ich bin außerdem zertifizierte Stoffwindelberaterin, Windelfrei Coach und Fachkraft für Babygeleitet Beikost (BLW).<br>Ich freue mich Euch in einem meiner Kurse kennenzulernen.</p>
    <p class="signature">Eure Carolina</p>
    <h2 class="founder-name">CAROLINA BRENNER</h2>
    <p class="founder-titles">Staatlich anerkannte Erzieherin -<br>Diplom Montessori Pädagogin i.A.<br>zertifizierte Stoffwindelberaterin /<br>Abhalte- und Windelfrei Coach,<br>Fachkraft für Babygeleitete Beikost</p>

    <svg style="left:317px;top:0" width="253" height="398" viewBox="0 0 253 398" role="img" aria-label="Foto der Kursleiterin mit Familie im herbstlichen Feld">
      <defs>
        <linearGradient id="familyTone" x1="0" y1="0" x2="0" y2="1">
          <stop offset="0" stop-color="#b9aab6"/>
          <stop offset=".45" stop-color="#8a6a4c"/>
          <stop offset="1" stop-color="#6d5232"/>
        </linearGradient>
      </defs>
      <path d="M50,0 L253,0 L253,330 C253,370 215,398 165,398 C95,398 0,360 0,280 L0,262 Z" fill="url(#familyTone)"/>
    </svg>

    <div class="hero-photo" role="img" aria-label="Foto einer lächelnden Mutter mit krabbelndem Baby und buntem Ball"></div>

    <div class="brand"><span class="brand-dot"></span>WALDKNIRPS</div>

    <h1 class="title-main">MONTESSORI</h1>
    <p class="title-sub">Eltern-Kind-Kurse</p>
    <p class="tagline">MONTESSORI PÄDAGOGIK FÜR BABYS UND KLEINKINDER</p>
    <p class="age-range">AB 8 WOCHEN BIS 4 JAHRE</p>

    <p class="contact" style="left:649px">INFO@WALDKNIRPS.DE</p>
    <p class="contact" style="left:776px">WWW. WALDKNIRPS.DE</p>
    <p class="contact" style="left:906px">WALDKNIRPS</p>
    <p class="contact" style="left:991px">WALDKNIRPS</p>

    <h2 class="section-title advice-title">Weiter Beratungsangebote:</h2>

    <div class="offer offer--diapers">
      <h3>Stoffwindel– und Windelfrei-Beratung:</h3>
      <p>Für alle Eltern, die sich für das Thema Stoffwindeln und Abhalten interessierenund gern mehr darüber erfahren möchten. Auch für (Stoffi)-Eltern, die Probleme haben oder etwas Neues ausprobieren wollen.</p>
      <ul>
        <li>Einzel- Paarberatung</li>
        <li>Workshops</li>
        <li>Stoffwindelparty</li>
        <li>Problemanalysen</li>
        <li>Miet- und Testpakete (ab Geburt – Trocken werden)</li>
      </ul>
    </div>

    <div class="offer offer--food">
      <h3>Beratung rund ums Thema:<br>Babygeleitete Beikost</h3>
      <p>Du möchtest wissen, was genau BLW ist und wie man es am besten umsetzt? Oder setzt es schon um, kommst aber nicht weiter? Dann ist eine individuelle Beratung genau das Richtige!</p>
      <ul>
        <li>Einzelberatungen</li>
        <li>Workshops</li>
      </ul>
    </div>
  </section>

  <!-- Inner side: play groups, coaching, course groups -->
  <section class="panel panel--inside">
    <svg class="backdrop" width="1139" height="570" viewBox="0 0 1139 570" aria-hidden="true">
      <polygon points="0,60 340,250 340,480 0,390" fill="var(--shade)"/>
      <polygon points="200,380 575,250 575,470" fill="var(--shade)" opacity=".8"/>
      <polygon points="575,120 860,280 860,570 575,570" fill="var(--shade)" opacity=".5"/>
    </svg>

    <h2 class="section-title" style="left:17px;top:10px;font-size:23px">Spielgruppen für Babys</h2>
    <p class="kicker" style="left:17px;top:38px;width:293px">Ab 8 Wochen – 4 Jahre</p>

    <div class="topic" style="left:17px;top:75px;width:302px">
      <h3>WAS IST MONTESSORI?</h3>
      <p class="topic-sub">Informationen zum pädagogischen Konzept</p>
      <p style="width:286px">In den Gruppenstunden liegt der Schwerpunkt auf der Beobachtung seines eigenen Kindes und der Eltern-Kind-Beziehung. Jedes Kind gestaltet seine Zeit ganz individuell nach seinen Bedürfnissen. Jede Gruppe hat einen individuell gestalteten Gruppenraum mit Montessori Material aus der Altersgruppe 0-3 Jahren sowie 3-6 Jahren.</p>
    </div>

    <div class="topic" style="left:17px;top:192px;width:262px">
      <h3>UMSETZUNG ZUHAUSE</h3>
      <p class="topic-sub">Anleitung der Eltern</p>
      <p style="width:256px;text-align:left">Zu jedem Thema bekommen die Eltern Unterstützung und Hilfestellung zur Umsetzung zu Hause. Im Elternportal der Website finden sie außerdem zusätzliche Tipps und Tricks.</p>
    </div>

    <div class="topic" style="left:15px;top:290px;width:314px">
      <h3>FAMILIEN-EVENTS</h3>
      <p class="topic-sub" style="width:200px">Austausch und Vernetzung</p>
      <p style="text-align:left">1x pro Kursblock findet ein Eltern - Event wie z.B. Eltern-Coaching, Sommerfest, Martinsumzug, etc. statt. Die Eltern können sich mit Teilnehmern aus anderen Kursen austauschen.</p>
    </div>

    <svg style="left:330px;top:0" width="238" height="376" viewBox="0 0 238 376" role="img" aria-label="Foto einer Mutter mit Baby im Arm vor herbstlichem Hintergrund">
      <defs>
        <linearGradient id="motherTone" x1="0" y1="0" x2="1" y2="1">
          <stop offset="0" stop-color="#c9a27a"/>
          <stop offset=".5" stop-color="#9a4a2c"/>
          <stop offset="1" stop-color="#6e4a36"/>
        </linearGradient>
      </defs>
      <path d="M47,0 L238,0 L238,290 C238,340 190,376 120,376 C50,376 0,330 0,262 L0,205 Z" fill="url(#motherTone)"/>
    </svg>

    <svg style="left:0;top:376px" width="229" height="194" viewBox="0 0 229 194" role="img" aria-label="Foto feiernder Kinder an einem Geburtstagstisch mit Luftballons">
      <defs>
        <linearGradient id="partyTone" x1="0" y1="0" x2="0" y2="1">
          <stop offset="0" stop-color="#8bbd5a"/>
          <stop offset=".55" stop-color="#e5a3b8"/>
          <stop offset="1" stop-color="#e9c26a"/>
        </linearGradient>
      </defs>
      <path d="M0,40 C40,5 150,0 200,40 C229,70 229,120 229,194 L0,194 Z" fill="url(#partyTone)"/>
    </svg>

    <h2 class="section-title coaching-title">Montessori Coaching für Zuhause</h2>
    <p class="kicker coaching-kicker">Ab Babyalter - Preschool Alter</p>

    <div class="coaching" style="left:262px;top:450px;width:300px">
      <p>Wir gestalten zusammen Euer individuelles Zuhause nach den Prinzipien der Montessori Pädagogik.</p>
      <p style="margin-top:8px;margin-bottom:3px">WIE LÄUFT EIN MONTESSORI COACHING AB?</p>
      <p>Das Coaching besteht aus 3 Hausbesuchen, die jeweils ca. 2 Stunden dauern und sich über einen Zeitraum von 6-8 Wochen erstrecken.</p>
    </div>

    <h2 class="section-title" style="left:592px;top:10px;font-size:23px">Gruppeneinteilung</h2>

    <div class="course" style="left:592px;top:56px;width:225px">
      <h3>BABY KURSE</h3>
      <p class="course-sub" style="margin-left:44px">ab 8 Wochen bis 6 Monate</p>
      <p style="margin-left:3px;width:217px">Im Baby Kurs lernen die Teilnehmer unter anderem die verschiedenen Montessori Mobiles kennen. Wir sprechen über Themen wie z.B.: Ernährung, bedürfnisorientiertes Wickeln, Eingewöhnung in die KITA und noch vieles mehr.</p>
    </div>

    <div class="course" style="left:592px;top:189px;width:234px">
      <h3>CRAWLER KURSE</h3>
      <p class="course-sub" style="margin-left:46px">ab 6 Monaten bis ca.15 Monate</p>
      <p>Im Crawler Kurs findet eine gemeinsame Brotzeit nach BLW statt. Ein Montessori Spiegel mit integrierter Pull-up-Stange lädt die Kinder zum Hochziehen ein. Die Kinder finden außerdem Montessori Material für ihre Altersgruppe.</p>
    </div>

    <div class="course" style="left:592px;top:329px;width:291px">
      <h3>TODDLER KURSE</h3>
      <p class="course-sub" style="margin-left:43px">ab ca. 15 Monaten bis max. 36 Monate</p>
      <p style="margin-left:3px;text-align:left">In den Toddler Kursen liegt der Schwerpunkt auf den Dingen des täglichen Lebens und auf der Entwicklung zur Selbständigkeit. So können sie sich selbst Essen zu bereiten, sich selbst ein Glas Wasser einschenken und noch vieles mehr.</p>
    </div>

    <div class="course" style="left:592px;top:446px;width:360px">
      <h3>PRESCOOLER KURSE</h3>
      <p class="course-sub" style="margin-left:48px">ab 2 Jahren bis max. 4 Jahre</p>
      <p style="margin-left:3px;text-align:left">Im Preschooler Kurs haben die Kinder neben den Übungen des täglichen Lebens noch zusätzlich die Möglichkeit, erste Erfahrungen mit Buchstaben und Zahlen, sowie mit Geografie-Material zu machen.</p>
    </div>

    <p class="footer-line">MONTESSORI PÄDAGOGIK FÜR BABYS UND KLEINKINDER</p>

    <svg style="left:831px;top:0" width="308" height="570" viewBox="0 0 308 570" aria-hidden="true">
      <defs>
        <linearGradient id="babyBedTone" x1="0" y1="0" x2="1" y2="1">
          <stop offset="0" stop-color="#e2d8d4"/>
          <stop offset="1" stop-color="#f4eeec"/>
        </linearGradient>
        <linearGradient id="crawlerTone" x1="0" y1="0" x2="1" y2="1">
          <stop offset="0" stop-color="#c9a57c"/>
          <stop offset=".6" stop-color="#e6cdb8"/>
          <stop offset="1" stop-color="#b9c4d4"/>
        </linearGradient>
        <linearGradient id="shelfTone" x1="0" y1="0" x2="0" y2="1">
          <stop offset="0" stop-color="#d9d2c8"/>
          <stop offset=".6" stop-color="#e8d6bc"/>
          <stop offset="1" stop-color="#7fa8c9"/>
        </linearGradient>
      </defs>
      <path role="img" aria-label="Foto eines liegenden Neugeborenen auf weißer Decke" d="M40,0 L308,0 L308,140 L30,140 C10,100 12,40 40,0 Z" fill="url(#babyBedTone)"/>
      <path role="img" aria-label="Foto eines krabbelnden Kleinkinds" d="M0,142 L308,142 L308,328 L30,328 C10,280 0,210 0,142 Z" fill="url(#crawlerTone)"/>
      <path role="img" aria-label="Foto eines Montessori-Regals mit Alltagsmaterial und Globen" d="M51,330 L308,330 L308,570 L215,570 C175,545 80,450 51,330 Z" fill="url(#shelfTone)"/>
    </svg>
  </section>

</div>
</body>
</html>
```